PROPERTY DEVELOPERS - LOGO & STATIONERY

We require a new logo design for a property development and sales company in Sydney, Australia.

We source land, build and sell residential & commercial investment properties including apartment buildings, townhouses, house and land packages in estates and retail shops.

We sell to local and overseas markets therefore the design needs to be a corporate effective global logo that would also suit the Asian market.

The company name is Corvane and we have been operating for 11 years and have been involved with over 5,000 properties. The focus should be on our company name Corvane with the word property as the word to explain ourselves.

This brief includes the logo design, business cards, letterhead, envelopes, with compliments slips and address label stickers.

We look forward to receiving exciting new designs.
All the best.

Reason: Designer who we were going to choose had their account closed.  Need some more options!

Industry/Entity Type

Property

Logo Text

Corvane Property

```html
<!DOCTYPE html>
<html lang="en">
<head>
<meta charset="utf-8">
<title>Corvane Property — Letterhead</title>
<link rel="stylesheet" href="https://fonts.googleapis.com/css2?family=Urbanist:wght@500;700&display=swap">
<style>
  :root {
    --ink: #0c3a3e;
    --deep: #04282c;
    --amber: #f79d1e;
    --paper: #ffffff;
    --edge: #8a8f91;
  }
  * { margin: 0; padding: 0; box-sizing: border-box; }
  html, body {
    width: 849px;
    height: 1200px;
    overflow: hidden;
    background: var(--paper);
  }
  .letterhead {
    position: relative;
    width: 849px;
    height: 1200px;
    background: var(--paper);
    border: 1px solid var(--edge);
    font-family: "Urbanist", "Century Gothic", sans-serif;
    font-weight: 500;
    color: var(--ink);
    overflow: hidden;
  }
  .top-band-amber {
    position: absolute; left: 0; top: 0;
    width: 581px; height: 26px;
    background: var(--amber);
  }
  .top-band-deep {
    position: absolute; left: 581px; top: 0;
    right: 0; height: 26px;
    background: var(--deep);
  }
  .side-rail {
    position: absolute; left: 822px; top: 0;
    width: 27px; height: 1200px;
    background: var(--deep);
  }
  .side-rail-accent {
    position: absolute; left: 822px; top: 1096px;
    width: 27px; height: 104px;
    background: var(--amber);
  }
  .brand {
    position: absolute;
    left: 573px; top: 56px;
    width: 145px;
    height: 144px;
    display: flex;
    flex-direction: column;
    align-items: center;
    justify-content: center;
    gap: 12px;
  }
  .brand-square {
    width: 44px; height: 44px;
    background: var(--deep);
  }
  .brand-name {
    font-size: 24px;
    font-weight: 700;
    line-height: 1.1;
    text-align: center;
    color: var(--deep);
  }
  .contact {
    position: absolute;
    left: 581px; top: 213px;
    font-size: 12.4px;
    line-height: 17.1px;
    font-style: normal;
    white-space: nowrap;
  }
  .contact strong { font-weight: 700; }
  .dot {
    display: inline-block;
    width: 4px; height: 4px;
    border-radius: 50%;
    background: var(--amber);
    margin: 0 6px;
    vertical-align: middle;
  }
  .registered {
    position: absolute;
    left: 581px; top: 1093px;
    font-size: 10.8px;
    line-height: 15.6px;
    font-style: normal;
    white-space: nowrap;
  }
</style>
</head>
<body>
  <main class="letterhead">
    <div class="top-band-amber"></div>
    <div class="top-band-deep"></div>
    <div class="side-rail"></div>
    <div class="side-rail-accent"></div>

    <header class="brand">
      <div class="brand-square"></div>
      <div class="brand-name">Corvane Property</div>
    </header>

    <address class="contact">
      Corvane Property<span class="dot"></span>48 Harbour Lane<br>
      Darling Quarter<span class="dot"></span>Inner West<br>
      NSW<span class="dot"></span>2009<br>
      <strong>Tel:</strong> 02 9384 1170 <strong>Fax:</strong> 02 9384 1171<br>
      <strong>email:</strong> sales@corvaneproperty.co.au<br>
      www.corvaneproperty.com
    </address>

    <address class="registered">
      Registered Office: Corvane Property<br>
      48 Harbour Lane<span class="dot"></span>Darling Quarter<br>
      Inner West<span class="dot"></span>NSW<span class="dot"></span>2009<br>
      ABN 58 203 144 761
    </address>
  </main>
</body>
</html>
```